Emergency Medical Training and Events Company Business Needs Business Card Design

We are in need of a business card for our dynamic company expanding its customer base and need to be easily contacted and identified for when we visit with government officials, potential EMS / Fire agencies and county coordinators to arrange for training programs for first responders to better prepare them for critical thinking at critical incidents.

Target Market(s)

EMS/Fire and Event Promoters

Industry/Entity Type

Medical

Contact Information for Business Card

Two cards, comparable designs:

Martin K. Halvey, Principal, m.halvey@rvqtlo.com
Owen Tash, Event and Training Specialist, o.tash@rvqtlo.com

Font styles to use
Other font styles liked:
• Cambria

Colors

Designer to choose colors to be used in the design.

Requirements
Must have
• Company Logo, Spots for Name, Title, Phone Number, Email, Website
• A bullet list stating that we offer, QRB CPR and First Aid Instructors, Hold the Line Instructors, Event EMS, CME's, MCI Training and Planning. We prefer to have a black background for the card but if you can make a blue or white card stand out we would review that as well.
Should not have
• Tacky logos or special sayings ... simple, elegant, professional is the look we seek

```html
<!DOCTYPE html>
<html lang="en">
<head>
<meta charset="utf-8">
<title>Riverquay Business Cards</title>
<link href="https://fonts.googleapis.com/css2?family=Roboto+Condensed:wght@400;700&family=Noto+Serif:wght@400;700&display=swap" rel="stylesheet">
<style>
  :root {
    --navy: #1b1f4e;
    --red: #c8191e;
    --mist: #e6e6e8;
    --paper: #ffffff;
    --ink: #1d1d24;
    --stage: #dedede;
  }
  * { margin: 0; padding: 0; box-sizing: border-box; }
  html, body { width: 1200px; height: 900px; overflow: hidden; }
  body { background: var(--stage); position: relative; font-family: "Noto Serif", serif; }

  .card {
    position: absolute;
    width: 627px;
    border-radius: 24px;
    overflow: hidden;
    box-shadow: 0 10px 22px rgba(0,0,0,0.18);
    transform: scale(0.893);
    transform-origin: top left;
  }

  /* Front */
  .card-front { left: 320px; top: 50px; height: 360px; background: var(--mist); }
  .front-band {
    position: absolute; left: 0; top: 0; width: 100%; height: 217px;
    background: var(--navy); border-bottom: 5px solid var(--red);
  }
  .brand-mark {
    position: absolute; left: 138px; top: 64px; width: 90px; height: 90px;
    border-radius: 50%; background: var(--paper);
  }
  .brand-divider {
    position: absolute; left: 245px; top: 68px; width: 2px; height: 82px; background: var(--red);
  }
  .brand-name {
    position: absolute; left: 262px; top: 79px;
    font-family: "Roboto Condensed", sans-serif; font-weight: 700;
    font-size: 52px; line-height: 60px; color: var(--paper); letter-spacing: 1px;
  }
  .front-company {
    position: absolute; left: 0; right: 0; top: 252px; text-align: center;
    font-family: "Roboto Condensed", sans-serif; color: var(--red);
  }
  .front-company .line-main { font-weight: 700; font-size: 40px; line-height: 44px; }
  .front-company .line-sub { font-weight: 400; font-size: 23px; line-height: 30px; margin-top: 4px; }

  /* Back */
  .card-back { top: 430px; height: 358px; background: var(--paper); }
  .card-back.holder-one { left: 25px; }
  .card-back.holder-two { left: 615px; }
  .back-strip { position: absolute; left: 0; top: 0; width: 78px; height: 100%; background: var(--navy); }
  .back-strip-accent { position: absolute; left: 0; top: 44px; width: 78px; height: 50px; background: var(--red); }

  .person { position: absolute; left: 94px; top: 42px; }
  .person-name { font-size: 27px; line-height: 34px; color: var(--ink); }
  .person-name .given { color: var(--red); font-weight: 700; }
  .person-title { font-size: 16px; line-height: 20px; color: var(--ink); }

  .services { position: absolute; left: 94px; top: 112px; list-style: none; }
  .services li {
    position: relative; padding-left: 14px;
    font-size: 12px; line-height: 19px; color: var(--ink);
  }
  .services li::before {
    content: ""; position: absolute; left: 0; top: 7px;
    width: 6px; height: 6px; background: var(--red);
  }

  .contact-icons { position: absolute; left: 39px; top: 220px; list-style: none; }
  .contact-icons li { width: 26px; height: 26px; margin-bottom: 4px; }

  .contact-list { position: absolute; left: 94px; top: 219px; list-style: none; }
  .contact-list li { font-weight: 700; font-size: 18px; line-height: 30px; color: var(--ink); }

  .faint-mark {
    position: absolute; left: 396px; top: 109px; width: 140px; height: 140px;
    border-radius: 50%; background: rgba(200,25,30,0.08);
  }
  .back-company {
    position: absolute; left: 300px; width: 325px; top: 256px; text-align: center;
    font-size: 17px; line-height: 22px; color: var(--red);
  }
</style>
</head>
<body>

<section class="card card-front" aria-label="Card front">
  <div class="front-band">
    <div class="brand-mark"></div>
    <div class="brand-divider"></div>
    <div class="brand-name">RIVERQUAY</div>
  </div>
  <div class="front-company">
    <div class="line-main">RIVERQUAY VENUE &amp;</div>
    <div class="line-sub">TRAINING LOGISTICS OF ONTARIO,LLC</div>
  </div>
</section>

<section class="card card-back holder-one" aria-label="Card back, Martin K. Halvey">
  <div class="back-strip"></div>
  <div class="back-strip-accent"></div>

  <div class="person">
    <div class="person-name"><span class="given">MARTIN K.</span> HALVEY</div>
    <div class="person-title">PRINCIPAL</div>
  </div>

  <ul class="services">
    <li>QRB CPR and First Aid Instructors</li>
    <li>Hold the Line Instructors</li>
    <li>Event EMS</li>
    <li>CME's</li>
    <li>MCI Training and Planning</li>
  </ul>

  <ul class="contact-icons">
    <li>
      <svg width="26" height="26" viewBox="0 0 26 26" aria-label="Phone">
        <circle cx="13" cy="13" r="12" fill="none" stroke="#ffffff" stroke-width="1"/>
        <path d="M7.5 11 Q13 6.5 18.5 11 L17 12.5 L15 11.5 L15 10 Q13 9.2 11 10 L11 11.5 L9 12.5 Z" fill="#c8191e"/>
        <rect x="8.5" y="13" width="9" height="5.5" rx="1" fill="#c8191e"/>
      </svg>
    </li>
    <li>
      <svg width="26" height="26" viewBox="0 0 26 26" aria-label="Email">
        <circle cx="13" cy="13" r="12" fill="none" stroke="#ffffff" stroke-width="1"/>
        <rect x="7.5" y="9.5" width="11" height="7.5" fill="#c8191e"/>
        <path d="M7.5 9.5 L13 14 L18.5 9.5" fill="none" stroke="#ffffff" stroke-width="0.8"/>
      </svg>
    </li>
    <li>
      <svg width="26" height="26" viewBox="0 0 26 26" aria-label="Website">
        <circle cx="13" cy="13" r="12" fill="none" stroke="#ffffff" stroke-width="1"/>
        <circle cx="13" cy="13" r="6" fill="#c8191e"/>
        <path d="M7 13 H19 M13 7 V19 M9 9.5 Q13 11 17 9.5 M9 16.5 Q13 15 17 16.5" fill="none" stroke="#ffffff" stroke-width="0.7"/>
      </svg>
    </li>
  </ul>

  <ul class="contact-list">
    <li>555 014 2290</li>
    <li>m.halvey@rvqtlo.com</li>
    <li>www.rvqtlo.com</li>
  </ul>

  <div class="faint-mark"></div>
  <div class="back-company">Riverquay Venue &amp;<br>Training Logistics of Ontario,LLC</div>
</section>

<section class="card card-back holder-two" aria-label="Card back, Owen Tash">
  <div class="back-strip"></div>
  <div class="back-strip-accent"></div>

  <div class="person">
    <div class="person-name"><span class="given">OWEN</span> TASH</div>
    <div class="person-title">EVENT AND TRAINING SPECIALIST</div>
  </div>

  <ul class="services">
    <li>QRB CPR and First Aid Instructors</li>
    <li>Hold the Line Instructors</li>
    <li>Event EMS</li>
    <li>CME's</li>
    <li>MCI Training and Planning</li>
  </ul>

  <ul class="contact-icons">
    <li>
      <svg width="26" height="26" viewBox="0 0 26 26" aria-label="Phone">
        <circle cx="13" cy="13" r="12" fill="none" stroke="#ffffff" stroke-width="1"/>
        <path d="M7.5 11 Q13 6.5 18.5 11 L17 12.5 L15 11.5 L15 10 Q13 9.2 11 10 L11 11.5 L9 12.5 Z" fill="#c8191e"/>
        <rect x="8.5" y="13" width="9" height="5.5" rx="1" fill="#c8191e"/>
      </svg>
    </li>
    <li>
      <svg width="26" height="26" viewBox="0 0 26 26" aria-label="Email">
        <circle cx="13" cy="13" r="12" fill="none" stroke="#ffffff" stroke-width="1"/>
        <rect x="7.5" y="9.5" width="11" height="7.5" fill="#c8191e"/>
        <path d="M7.5 9.5 L13 14 L18.5 9.5" fill="none" stroke="#ffffff" stroke-width="0.8"/>
      </svg>
    </li>
    <li>
      <svg width="26" height="26" viewBox="0 0 26 26" aria-label="Website">
        <circle cx="13" cy="13" r="12" fill="none" stroke="#ffffff" stroke-width="1"/>
        <circle cx="13" cy="13" r="6" fill="#c8191e"/>
        <path d="M7 13 H19 M13 7 V19 M9 9.5 Q13 11 17 9.5 M9 16.5 Q13 15 17 16.5" fill="none" stroke="#ffffff" stroke-width="0.7"/>
      </svg>
    </li>
  </ul>

  <ul class="contact-list">
    <li>555 014 2290</li>
    <li>o.tash@rvqtlo.com</li>
    <li>www.rvqtlo.com</li>
  </ul>

  <div class="faint-mark"></div>
  <div class="back-company">Riverquay Venue &amp;<br>Training Logistics of Ontario,LLC</div>
</section>

</body>
</html>
```